Shopify Web-Page "Kids-LoomNestery

We are building a new business in Switzerland offering premium sewing holiday camps for kids aged 9–14. In enclosed brief outlines our requirements for a complete Shopify homepage design and a multilingual logo creation.
Domains: kids-loomnest.example ; kids-nidotelaio.example ; kids-webnest.example

Project Overview
We are looking for:
1. A modern, fully designed Shopify homepage in English using standard Shopify content blocks (no custom coding), which we can later update ourselves. Supporting Multilanguage (EN, German, Italian).

2. A logo design that includes the brand identity and communicates our multilingual, creative, and child-focused positioning.

All details in enclosed

```html
<!DOCTYPE html>
<html lang="en">
<head>
<meta charset="utf-8">
<title>Kids-LoomNestery – Sewing Camps for Kids</title>
<link href="https://fonts.googleapis.com/css2?family=Poppins:wght@400;500;600;700&display=swap" rel="stylesheet">
<style>
:root{
  --coral:#f26d5b;
  --pink-bg:#fdecee;
  --pink-title:#de4677;
  --teal:#2aa8bf;
  --red:#e01e24;
  --orange:#f5a90a;
  --purple:#b36aa3;
  --sand:#f2dfae;
  --ink:#222;
  --muted:#555;
  --footer:#ef8278;
  --news:#fbe6e2;
  --card-line:#e6e6e6;
}
*{box-sizing:border-box;margin:0;padding:0}
html,body{width:1200px;height:4552px;overflow:hidden}
body{font-family:'Poppins',sans-serif;color:var(--ink);background:#fff;position:relative}
.abs{position:absolute}
.btn{position:absolute;display:flex;align-items:center;justify-content:center;background:var(--coral);color:#fff;border-radius:30px;font-size:11px;font-weight:500;text-transform:uppercase;box-shadow:0 0 0 2px #fff,0 0 0 4px var(--coral)}
.wave{position:absolute;left:0;width:1200px;display:block}

/* header */
.site-header{position:absolute;top:0;left:0;width:1200px;height:74px;background:#fff}
.logo{position:absolute;left:92px;top:4px;width:100px;height:118px;border-radius:50%;background:#fff;display:flex;align-items:center;justify-content:center;text-align:center;z-index:3}
.logo span{font-size:12px;font-weight:600;color:var(--teal);line-height:1.2}
.nav{position:absolute;top:30px;left:448px;display:flex;gap:34px;font-size:12px;font-weight:500}
.lang{position:absolute;top:30px;left:880px;font-size:12px}

/* hero */
.hero{position:absolute;top:74px;left:0;width:1200px;height:668px;background:radial-gradient(ellipse at 55% 40%,#fff5f6 0%,var(--pink-bg) 60%,#fbdfe3 100%)}
.hero h1{position:absolute;left:92px;top:232px;font-size:36px;line-height:45px;color:var(--pink-title);font-weight:600}
.hero p{position:absolute;left:92px;top:334px;width:400px;font-size:14px;line-height:24px}
.hero-photo{position:absolute;left:565px;top:89px;width:557px;height:500px;border-radius:58% 42% 48% 52% / 45% 55% 45% 55%;background:linear-gradient(140deg,#c38a55,#f2d8c4 45%,#e7b3b8 70%,#b9c7cf)}

/* about */
.about-photo{position:absolute;left:124px;top:836px;width:463px;height:374px;border-radius:55% 45% 50% 50% / 50% 45% 55% 50%;background:linear-gradient(135deg,#8a5a3c,#e9b89c 45%,#d45a5e 75%,#f3e2d4)}
.about-ring{position:absolute;left:124px;top:850px;width:450px;height:360px;border:2px solid #4a2f86;border-radius:50%;transform:rotate(-12deg)}
.about-text{position:absolute;left:636px;top:884px;width:440px}
.eyebrow{font-size:13px;color:var(--red);font-weight:500}
.about-text h2{font-size:36px;color:var(--teal);font-weight:600;line-height:44px;margin-bottom:10px}
.about-text p{font-size:13.5px;line-height:24px;margin-bottom:8px}

/* how */
.section-title{position:absolute;left:0;width:1200px;text-align:center;font-size:36px;font-weight:600}
.steps{position:absolute;top:1369px;left:101px;display:flex;gap:21px}
.step{width:182px;height:239px;background:#fff;border:1px solid var(--card-line);border-radius:6px;box-shadow:0 12px 24px rgba(0,0,0,.08);text-align:center;padding:34px 20px 0}
.step-icon{width:53px;height:53px;border-radius:10px;margin:0 auto 22px;display:flex;align-items:center;justify-content:center}
.step h3{font-size:14px;font-weight:600;margin-bottom:6px}
.step p{font-size:10.5px;line-height:15px;color:var(--muted)}

/* why */
.why{position:absolute;top:1770px;left:0;width:1200px;height:520px;background:var(--sand)}
.why h2{position:absolute;left:120px;top:152px;font-size:36px;font-weight:600}
.why ul{position:absolute;left:126px;top:212px;list-style:none;font-size:14px;line-height:26.5px}
.why li{display:flex;align-items:center;gap:6px}
.tick{width:15px;height:15px;border-radius:3px;background:#4caf50;display:inline-flex;align-items:center;justify-content:center}
.why-photo{position:absolute;left:618px;top:60px;width:495px;height:460px;border-radius:50% 50% 40% 45% / 55% 55% 0 0;background:linear-gradient(160deg,#14c8b4,#18b9a6 40%,#c99a74 60%,#f2c230)}

/* camps */
.camps{position:absolute;top:2474px;left:159px;display:flex;gap:22px}
.camp{width:280px;height:353px;background:#fff;border:1px solid var(--card-line);border-radius:6px;box-shadow:0 10px 22px rgba(0,0,0,.07);padding:14px 14px 0}
.camp-photo{height:191px;border-radius:3px}
.camp h3{font-size:17px;font-weight:500;margin:20px 0 4px 8px}
.camp p{font-size:10px;color:var(--muted);margin-left:8px}
.camp .btn{position:relative;width:117px;height:34px;margin:18px 0 0 8px}

/* cta */
.cta{position:absolute;top:2937px;left:0;width:1200px;height:363px;background:linear-gradient(120deg,#3c3a38,#6b4f47 40%,#8a5d52 60%,#3f3c3b)}
.cta h2{position:absolute;top:120px;width:1200px;text-align:center;font-size:36px;color:var(--orange);font-weight:600}
.cta p{position:absolute;top:177px;width:1200px;text-align:center;font-size:14px;color:#fff}

/* faq */
.faq{position:absolute;top:3467px;left:276px;width:646px}
.faq-item{height:47px;border:1px solid #ccc;border-radius:24px;margin-bottom:11.5px;display:flex;align-items:center;justify-content:space-between;padding:0 16px 0 30px;font-size:15px;font-weight:500;border-bottom:1px dashed #bbb}
.plus{width:17px;height:17px;border-radius:50%;display:flex;align-items:center;justify-content:center}

/* newsletter */
.news{position:absolute;top:3880px;left:0;width:1200px;height:320px;background:var(--news)}
.news h2{position:absolute;left:141px;top:148px;font-size:36px;color:var(--red);font-weight:600}
.news p{position:absolute;left:141px;top:200px;font-size:14px}
.news-form{position:absolute;left:603px;top:156px;width:440px;height:56px;background:#fff;border-radius:28px}
.news-form span{position:absolute;left:25px;top:19px;font-size:11px}
.news-form .btn{right:0;top:0;width:152px;height:56px;background:var(--purple);box-shadow:none;text-transform:none;font-size:12px}

/* footer */
.footer{position:absolute;top:4200px;left:0;width:1200px;height:352px;background:var(--footer);color:#fff}
.f-logo{position:absolute;left:186px;top:88px;width:88px;height:88px;border-radius:50%;border:2px solid #fff;display:flex;align-items:center;justify-content:center;text-align:center;font-size:10px;font-weight:600}
.f-tag{position:absolute;left:128px;top:193px;width:210px;text-align:center;font-size:10px;line-height:14px}
.f-col{position:absolute;top:93px;font-size:12px;line-height:24px}
.f-col h4{font-size:16px;font-weight:500;margin-bottom:2px}
.social{position:absolute;left:896px;top:124px;display:flex;gap:14px}
.social i{display:block;width:28px;height:28px;border-radius:50%}
.copy{position:absolute;top:312px;width:1200px;text-align:center;font-size:12px}
.totop{position:absolute;left:1124px;top:228px;width:32px;height:32px;border-radius:50%;background:#7fa8d9}
</style>
</head>
<body>

<header class="site-header">
  <div class="logo"><span>Kids-<br>LoomNestery</span></div>
  <nav class="nav">
    <svg width="14" height="14" viewBox="0 0 14 14" aria-label="Home"><path d="M2 7L7 2l5 5M3.5 6v6h7V6" fill="none" stroke="#222" stroke-width="1.3"/></svg>
    <span>ABOUT</span><span>CAMPS</span><span>FAQ</span><span>CONTACT</span>
  </nav>
  <div class="lang">EN &nbsp;|&nbsp; DE &nbsp;|&nbsp; IT</div>
  <div class="btn" style="left:975px;top:18px;width:131px;height:38px">Book a camp</div>
</header>

<section class="hero">
  <h1>Premium Sewing Camps<br>for Kids in Switzerland</h1>
  <p>A creative, fun, and inspiring holiday experience for children aged 9–14.</p>
  <div class="btn" style="left:92px;top:397px;width:200px;height:35px">View upcoming camps</div>
  <div class="hero-photo" role="img" aria-label="Smiling girl working at a sewing machine"></div>
</section>
<svg class="wave" style="top:726px" height="32" viewBox="0 0 1200 32" aria-hidden="true">
  <defs><pattern id="waveHero" width="70" height="32" patternUnits="userSpaceOnUse"><path d="M0 16 Q17.5 0 35 16 T70 16 V0 H0Z" fill="#fbdfe3"/></pattern></defs>
  <rect width="1200" height="32" fill="url(#waveHero)"/>
</svg>

<section class="about">
  <div class="about-ring"></div>
  <div class="about-photo" role="img" aria-label="Instructor and girl sewing together at a table"></div>
  <div class="about-text">
    <div class="eyebrow">About Us</div>
    <h2>Meet Lena &amp; Mara</h2>
    <p>With over 10 years of experience teaching sewing, tailoring, and design, we guide young talents through a creative week full of fun, structure, and style.</p>
    <p>Small groups (max. 8 children) ensure personal attention and great results — from handmade creations to a cheerful fashion show on the final day!</p>
  </div>
  <div class="btn" style="left:636px;top:1131px;width:129px;height:33px">Book a camp</div>
</section>

<h2 class="section-title" style="top:1285px;color:var(--red)">How the camp works</h2>
<div class="steps">
  <div class="step"><div class="step-icon" style="background:#e5262a"><svg width="26" height="22" viewBox="0 0 26 22"><circle cx="13" cy="5" r="3.5" fill="#fff"/><circle cx="5" cy="9" r="2.8" fill="#fff"/><circle cx="21" cy="9" r="2.8" fill="#fff"/><path d="M7 22a6 6 0 0 1 12 0Z M0 22a5 5 0 0 1 9-2v2Z M26 22a5 5 0 0 0-9-2v2Z" fill="#fff"/></svg></div><h3>Project selection</h3><p>Your child chooses their own model based on previously produced clothing items and sewing patterns.</p></div>
  <div class="step"><div class="step-icon" style="background:#f4a6ae"><svg width="26" height="26" viewBox="0 0 26 26"><rect x="3" y="3" width="20" height="20" rx="4" fill="none" stroke="#fff" stroke-width="2" stroke-dasharray="3 2"/></svg></div><h3>Fabric selection</h3><p>High-quality fabrics are available.</p></div>
  <div class="step"><div class="step-icon" style="background:#1fae9a"><svg width="28" height="22" viewBox="0 0 28 22"><path d="M2 20h24M4 20V6h18v6H10v8" fill="none" stroke="#fff" stroke-width="2.4"/></svg></div><h3>Sewing machine</h3><p>Operation – Learn how to use a sewing machine.</p></div>
  <div class="step"><div class="step-icon" style="background:#f5a623"><svg width="24" height="24" viewBox="0 0 24 24"><path d="M4 20L20 4" stroke="#fff" stroke-width="2.5"/><circle cx="18" cy="6" r="3" fill="none" stroke="#fff" stroke-width="2"/></svg></div><h3>Sewing &amp; refining</h3><p>Step by step to the goal with professional guidance.</p></div>
  <div class="step"><div class="step-icon" style="background:#7ab648"><svg width="24" height="24" viewBox="0 0 24 24"><circle cx="8" cy="5" r="3" fill="#fff"/><circle cx="16" cy="5" r="3" fill="#fff"/><rect x="5" y="9" width="6" height="13" rx="2" fill="#fff"/><rect x="13" y="9" width="6" height="13" rx="2" fill="#fff"/></svg></div><h3>Showtime!</h3><p>Fashion show or photo shoot at the end of the week</p></div>
</div>

<svg class="wave" style="top:1740px" height="32" viewBox="0 0 1200 32" aria-hidden="true">
  <defs><pattern id="waveWhyTop" width="70" height="32" patternUnits="userSpaceOnUse"><path d="M0 16 Q17.5 0 35 16 T70 16 V32 H0Z" fill="#f2dfae"/></pattern></defs>
  <rect width="1200" height="32" fill="url(#waveWhyTop)"/>
</svg>
<section class="why">
  <h2>Why Parents Choose Us</h2>
  <ul>
    <li><span class="tick"><svg width="10" height="10"><path d="M1 5l3 3 5-6" stroke="#fff" stroke-width="2" fill="none"/></svg></span>Small groups &amp; personalized attention</li>
    <li><span class="tick"><svg width="10" height="10"><path d="M1 5l3 3 5-6" stroke="#fff" stroke-width="2" fill="none"/></svg></span>Multilingual supervision (DE / EN / IT)</li>
    <li><span class="tick"><svg width="10" height="10"><path d="M1 5l3 3 5-6" stroke="#fff" stroke-width="2" fill="none"/></svg></span>High-quality fabrics &amp; top-quality sewing machines (Stichwerk)</li>
    <li><span class="tick"><svg width="10" height="10"><path d="M1 5l3 3 5-6" stroke="#fff" stroke-width="2" fill="none"/></svg></span>Encouragement of creativity, self-confidence, and fine motor skills</li>
    <li><span class="tick"><svg width="10" height="10"><path d="M1 5l3 3 5-6" stroke="#fff" stroke-width="2" fill="none"/></svg></span>Safe, loving environment in Zurich, various places easy to reach</li>
    <li><span class="tick"><svg width="10" height="10"><path d="M1 5l3 3 5-6" stroke="#fff" stroke-width="2" fill="none"/></svg></span>Pick-up Service from the Main-Station</li>
  </ul>
  <div class="why-photo" role="img" aria-label="Happy family of three on a turquoise background"></div>
</section>
<svg class="wave" style="top:2290px" height="32" viewBox="0 0 1200 32" aria-hidden="true">
  <defs><pattern id="waveWhyBottom" width="70" height="32" patternUnits="userSpaceOnUse"><path d="M0 16 Q17.5 32 35 16 T70 16 V0 H0Z" fill="#f2dfae"/></pattern></defs>
  <rect width="1200" height="32" fill="url(#waveWhyBottom)"/>
</svg>

<h2 class="section-title" style="top:2393px;color:var(--orange)">Upcoming Sewing Camps</h2>
<div class="camps">
  <div class="camp"><div class="camp-photo" role="img" aria-label="Children in autumn park" style="background:linear-gradient(135deg,#c9a23a,#b6432f 50%,#3a4e7a)"></div><h3>Spring Camp 2025</h3><p>Zurich — Apr 7–11 • Ages 9–14</p><div class="btn">Book now</div></div>
  <div class="camp"><div class="camp-photo" role="img" aria-label="Children sitting together in a forest" style="background:linear-gradient(135deg,#2f5a2a,#7a8a4c 50%,#324a2b)"></div><h3>Summer Camp 2025</h3><p>Zurich — Jul 14–18 • Ages 9–14</p><div class="btn">Book now</div></div>
  <div class="camp"><div class="camp-photo" role="img" aria-label="Children playing in autumn leaves" style="background:linear-gradient(135deg,#b89a2a,#d9b23f 45%,#6f8a2c)"></div><h3>Autumn Camp 2025</h3><p>Zurich — Apr 7–11 • Ages 9–14</p><div class="btn">Book now</div></div>
</div>

<section class="cta" role="img" aria-label="Children in playful costumes, darkened background">
  <h2>Ready to Join the Fun?</h2>
  <p>Give your child a creative, unforgettable holiday!</p>
  <div class="btn" style="left:536px;top:210px;width:128px;height:34px">Book a camp</div>
</section>
<svg class="wave" style="top:2922px" height="32" viewBox="0 0 1200 32" aria-hidden="true">
  <defs><pattern id="waveCtaTop" width="70" height="32" patternUnits="userSpaceOnUse"><path d="M0 16 Q17.5 0 35 16 T70 16 V0 H0Z" fill="#fff"/></pattern></defs>
  <rect width="1200" height="32" fill="url(#waveCtaTop)"/>
</svg>
<svg class="wave" style="top:3284px" height="32" viewBox="0 0 1200 32" aria-hidden="true">
  <defs><pattern id="waveCtaBottom" width="70" height="32" patternUnits="userSpaceOnUse"><path d="M0 16 Q17.5 32 35 16 T70 16 V32 H0Z" fill="#fff"/></pattern></defs>
  <rect width="1200" height="32" fill="url(#waveCtaBottom)"/>
</svg>

<h2 class="section-title" style="top:3393px;color:var(--purple)">Frequently Asked Questions</h2>
<div class="faq">
  <div class="faq-item">Does my child need any prior sewing experience?<span class="plus" style="background:#e01e24"><svg width="9" height="9"><path d="M4.5 0v9M0 4.5h9" stroke="#fff" stroke-width="2"/></svg></span></div>
  <div class="faq-item">How does the pick-up service work?<span class="plus" style="background:#f4a6ae"><svg width="9" height="9"><path d="M4.5 0v9M0 4.5h9" stroke="#fff" stroke-width="2"/></svg></span></div>
  <div class="faq-item">How many clothing items will they make?<span class="plus" style="background:#1fae9a"><svg width="9" height="9"><path d="M4.5 0v9M0 4.5h9" stroke="#fff" stroke-width="2"/></svg></span></div>
  <div class="faq-item">What should my child bring?<span class="plus" style="background:#f5a623"><svg width="9" height="9"><path d="M4.5 0v9M0 4.5h9" stroke="#fff" stroke-width="2"/></svg></span></div>
  <div class="faq-item">What’s included in the camp fee?<span class="plus" style="background:#7ab648"><svg width="9" height="9"><path d="M4.5 0v9M0 4.5h9" stroke="#fff" stroke-width="2"/></svg></span></div>
  <div class="faq-item">What languages are spoken?<span class="plus" style="background:#f26d5b"><svg width="9" height="9"><path d="M4.5 0v9M0 4.5h9" stroke="#fff" stroke-width="2"/></svg></span></div>
</div>

<section class="news">
  <h2>Join Our Newsletter</h2>
  <p>Get updates about new camp dates and creative activities.</p>
  <div class="news-form"><span>Enter your email</span><div class="btn">Subscribe Now</div></div>
</section>

<footer class="footer">
  <div class="f-logo">Kids-<br>LoomNestery</div>
  <div class="f-tag">Creative sewing holiday camps for kids aged 9–14 in Switzerland.</div>
  <div class="f-col" style="left:424px"><h4>Quick Links</h4>Home<br>Camps<br>About<br>FAQ<br>Contact</div>
  <div class="f-col" style="left:638px"><h4>Contact Info</h4>
    <svg width="9" height="11" viewBox="0 0 9 11"><path d="M4.5 11S0 6.5 0 4.5a4.5 4.5 0 0 1 9 0C9 6.5 4.5 11 4.5 11Z" fill="#fff"/></svg> Nadelgasse 4, 8001 Zurich<br>
    <svg width="11" height="8" viewBox="0 0 11 8"><rect width="11" height="8" fill="#fff"/><path d="M0 0l5.5 4L11 0" stroke="#ef8278" fill="none"/></svg> hello@loomnest.example<br>
    <svg width="10" height="10" viewBox="0 0 10 10"><path d="M2 0l2 3-1 1.5a6 6 0 0 0 2.5 2.5L7 6l3 2-1 2C4 10 0 6 0 1Z" fill="#fff"/></svg> +41 44 555 0190
  </div>
  <div class="social">
    <i style="background:#3b5998"></i><i style="background:#1da1f2"></i><i style="background:#dd4b39"></i><i style="background:#0e76a8"></i>
  </div>
  <div class="totop"></div>
  <div class="copy">©Copyright 2025 | All Rights Reserved</div>
</footer>
<svg class="wave" style="top:4184px" height="32" viewBox="0 0 1200 32" aria-hidden="true">
  <defs><pattern id="waveFooter" width="70" height="32" patternUnits="userSpaceOnUse"><path d="M0 16 Q17.5 0 35 16 T70 16 V32 H0Z" fill="#ef8278"/><path d="M0 16 Q17.5 0 35 16 T70 16 V0 H0Z" fill="#fbe6e2"/></pattern></defs>
  <rect width="1200" height="32" fill="url(#waveFooter)"/>
</svg>

</body>
</html>
```